Home Remodeler Needs a Website!

Single page (plus contact form) website for small home remodeling company. He's got a few pictures he'd like on the site and needs some basic text. He likes clean, simple designs and is "more traditional" in his stylistic preferences. Most of his business comes from word-of-mouth advertising and so the site is just something he needs for people to feel more comfortable with his business.

Target Market(s)

People who want to remodel their homes

Coding

Coded - Design and coding required

Number of Pages Required

2 page

Requirements
Must have
• Main page to include some or all of the attached images, contact page. Neutral colors. Old domain: brindlecoveabodes.com New domain: qm-holdings.com You can pull text from the old site or update it.
Should not have
• No loud colors/loud visual elements

```html
<!DOCTYPE html>
<html lang="en">
<head>
<meta charset="utf-8">
<title>Brindle Cove Homes</title>
<link href="https://fonts.googleapis.com/css2?family=Montserrat:wght@400;600;700&family=Raleway:wght@300;400&display=swap" rel="stylesheet">
<style>
:root{
  --black:#000;
  --ink:#0b0b0b;
  --panel:#1c1c1c;
  --form-bg:#1a1a1a;
  --field:#141414;
  --field-line:#3a3a3a;
  --white:#fff;
  --grey:#bdbdbd;
  --muted:#8c8c8c;
  --orange:#f07a1a;
  --orange-dark:#e0620e;
}
*{margin:0;padding:0;box-sizing:border-box}
html,body{width:1200px;height:3424px;overflow:hidden;background:var(--black)}
body{position:relative;font-family:"Montserrat",sans-serif;color:var(--white)}
.abs{position:absolute}

/* header */
.site-header{position:absolute;left:0;top:0;width:1200px;height:76px;background:rgba(0,0,0,.55);z-index:5}
.brand{position:absolute;left:64px;top:28px;font:700 17px "Montserrat",sans-serif;letter-spacing:.5px}
.main-nav{position:absolute;left:410px;top:32px;display:flex;gap:62px;font:600 11px "Montserrat",sans-serif;letter-spacing:1px}
.phone{position:absolute;left:946px;top:24px;display:flex;align-items:center;gap:12px;font:600 15px "Montserrat",sans-serif}
.phone-icon{width:28px;height:28px;border-radius:50%;background:var(--white);display:flex;align-items:center;justify-content:center}

/* hero */
.hero{position:absolute;left:0;top:0;width:1200px;height:762px;
  background:linear-gradient(180deg,rgba(0,0,0,.35),rgba(0,0,0,.45)),
  linear-gradient(110deg,#2b3a44 0%,#6b5846 25%,#8a7a68 45%,#4a3a2c 65%,#7c6a58 85%,#3c3a36 100%)}
.hero-title{position:absolute;left:0;top:296px;width:1200px;text-align:center;font:300 58px/64px "Raleway",sans-serif;letter-spacing:2px;text-transform:uppercase}
.btn-pill{position:absolute;height:44px;border-radius:22px;display:flex;align-items:center;justify-content:center;font:600 12px "Montserrat",sans-serif;letter-spacing:.5px;text-transform:uppercase}
.btn-light{background:var(--white);color:var(--black)}
.hero .btn-pill{left:510px;top:452px;width:180px}
.hero-arrow{position:absolute;top:366px}
.scroll-cue{position:absolute;left:0;top:664px;width:1200px;text-align:center;font:600 11px "Montserrat",sans-serif;letter-spacing:1.5px}

/* section headings */
.section-title{font:300 34px/40px "Raleway",sans-serif;text-transform:uppercase;letter-spacing:1px}
.rule{width:44px;height:2px;background:var(--white);margin:18px 0 26px}
.body-copy{font:400 13px/22px "Montserrat",sans-serif;color:var(--grey)}
.body-copy p{margin-bottom:16px}

/* welcome */
.welcome{position:absolute;left:0;top:762px;width:1200px;height:640px;background:var(--ink)}
.welcome .diamond{position:absolute;left:150px;top:140px}
.welcome .text{position:absolute;left:618px;top:122px;width:460px}

/* services band */
.services{position:absolute;left:0;top:1402px;width:1200px;height:560px}
.services .photo{position:absolute;left:0;top:0;width:1200px;height:560px;
  background:linear-gradient(100deg,#2a2622 0%,#5e5850 30%,#8b8276 55%,#a49886 75%,#6d655a 100%)}
.services .card{position:absolute;left:0;top:80px;width:648px;height:370px;background:rgba(28,28,28,.96);padding:62px 0 0 118px}
.services .section-title{font-size:30px;line-height:34px}
.services .rule{margin:16px 0 22px}
.service-list{display:flex;gap:60px;font:600 11px/19px "Montserrat",sans-serif;color:var(--white);margin-bottom:18px}
.services .note{font:400 11px/19px "Montserrat",sans-serif;color:var(--grey);width:400px;margin-bottom:18px}
.services .btn-pill{position:relative;width:150px;height:40px;font-size:11px}

/* tinker */
.tinker{position:absolute;left:0;top:1962px;width:1200px;height:728px;background:var(--ink)}
.tinker .text{position:absolute;left:118px;top:244px;width:430px}
.tinker .diamond{position:absolute;left:610px;top:146px}

/* contact */
.contact{position:absolute;left:0;top:2690px;width:1200px;height:540px;background:var(--form-bg);border-top:1px solid #2a2a2a}
.contact .section-title{position:absolute;left:0;top:78px;width:1200px;text-align:center;font-size:34px}
.contact .rule{position:absolute;left:578px;top:132px;margin:0}
.field{position:absolute;height:44px;background:var(--field);border:1px solid var(--field-line);font:400 11px "Montserrat",sans-serif;color:var(--muted);padding:15px 14px}
.contact .btn-send{left:498px;top:412px;width:190px;height:50px;border-radius:25px;background:linear-gradient(180deg,var(--orange),var(--orange-dark));color:var(--white);font-size:14px}

/* footer */
.site-footer{position:absolute;left:0;top:3230px;width:1200px;height:194px;background:var(--black)}
.footer-nav{position:absolute;left:0;top:50px;width:1200px;display:flex;justify-content:center;gap:100px;font:600 11px "Montserrat",sans-serif;letter-spacing:1px}
.legal{position:absolute;left:0;top:84px;width:1200px;text-align:center;font:400 11px "Montserrat",sans-serif;color:var(--grey)}
.social{position:absolute;left:538px;top:126px;display:flex;gap:14px}
.social span{width:32px;height:32px;border-radius:50%;background:var(--white)}
</style>
</head>
<body>

<section class="hero" role="img" aria-label="Photo of a renovated kitchen with stainless appliances, dark cabinets and stone counters">
  <svg class="hero-arrow" style="left:40px" width="24" height="40" viewBox="0 0 24 40"><path d="M20 4 4 20l16 16" fill="none" stroke="#fff" stroke-width="3"/></svg>
  <svg class="hero-arrow" style="left:1136px" width="24" height="40" viewBox="0 0 24 40"><path d="M4 4l16 16L4 36" fill="none" stroke="#fff" stroke-width="3"/></svg>
  <h1 class="hero-title">Your Dream<br>Luxury Renovation</h1>
  <span class="btn-pill btn-light">View Portfolio</span>
  <div class="scroll-cue">SCROLL<br>
    <svg width="22" height="14" viewBox="0 0 22 14" style="margin-top:6px"><path d="M2 2l9 9 9-9" fill="none" stroke="#fff" stroke-width="2"/></svg>
  </div>
</section>

<header class="site-header">
  <div class="brand">BRINDLE COVE HOMES</div>
  <nav class="main-nav"><span>HOME</span><span>SERVICES</span><span>ABOUT US</span><span>CONTACT US</span></nav>
  <div class="phone">
    <span class="phone-icon"><svg width="14" height="14" viewBox="0 0 24 24"><path d="M6.6 10.8a15 15 0 0 0 6.6 6.6l2.2-2.2a1 1 0 0 1 1-.25 11.4 11.4 0 0 0 3.6.57 1 1 0 0 1 1 1V20a1 1 0 0 1-1 1A17 17 0 0 1 3 4a1 1 0 0 1 1-1h3.5a1 1 0 0 1 1 1c0 1.25.2 2.45.57 3.57a1 1 0 0 1-.25 1z" fill="#000"/></svg></span>
    555-014-2280
  </div>
</header>

<section class="welcome">
  <svg class="diamond" width="360" height="360" viewBox="0 0 360 360" role="img" aria-label="Photo of a finished kitchen interior with warm lighting">
    <defs><linearGradient id="g1" x1="0" y1="0" x2="1" y2="1"><stop offset="0" stop-color="#4a3426"/><stop offset=".5" stop-color="#8a6a4e"/><stop offset="1" stop-color="#2a2018"/></linearGradient></defs>
    <polygon points="180,4 356,180 180,356 4,180" fill="none" stroke="#fff" stroke-width="2"/>
    <polygon points="180,22 338,180 180,338 22,180" fill="url(#g1)"/>
  </svg>
  <div class="text">
    <h2 class="section-title">Welcome to Brindle<br>Cove Homes</h2>
    <div class="rule"></div>
    <div class="body-copy">
      <p>When you want affordable, quality home construction services, think of us to do the job. Since 1981 Walter Dunmore has built and remodeled over 400 homes and businesses. Let us be your contractor for the next project you plan.</p>
      <p>When quality, value and personal attention to detail are important, with over 30 years experience in residential and commercial construction, you can trust your project to Brindle Cove Homes.</p>
      <p>"DON'T TINKER AROUND"</p>
    </div>
  </div>
</section>

<section class="services">
  <div class="photo" role="img" aria-label="Photo of an open living room with new hardwood flooring and french doors"></div>
  <div class="card">
    <h2 class="section-title">Commercial and<br>Residential Contracting</h2>
    <div class="rule"></div>
    <div class="service-list">
      <div>"ALL IN ONE PACKAGE"<br>Pre Construction Consultation<br>New Construction<br>Remodeling / Kitchens and baths</div>
      <div>Additions<br>Porches and Decks<br>Specializing in historic renovations</div>
    </div>
    <p class="note">Providing services for roofing, window replacement, electrical, air conditioning and plumbing upgrades, painting, gutters, concrete work.</p>
    <span class="btn-pill btn-light">Read More</span>
  </div>
</section>

<section class="tinker">
  <div class="text">
    <h2 class="section-title">Don't Tinker Around</h2>
    <div class="rule"></div>
    <div class="body-copy">
      <p>I have built my business with a partnership of clients, employees, subcontractors, suppliers and inspectors. Since each project is unique, this partnership brings creative ideas to your home.</p>
      <p>I have deep "hands on" history in construction from foundations to final finishing touches.</p>
      <p>We cultivate suppliers who deliver quality materials on time and without damage.</p>
    </div>
  </div>
  <svg class="diamond" width="420" height="420" viewBox="0 0 420 420" role="img" aria-label="Photo of a remodeled bathroom with a soaking tub and window">
    <defs><linearGradient id="g2" x1="0" y1="0" x2="1" y2="1"><stop offset="0" stop-color="#9aa4ac"/><stop offset=".5" stop-color="#c9c6bf"/><stop offset="1" stop-color="#6e6a64"/></linearGradient></defs>
    <polygon points="210,4 416,210 210,416 4,210" fill="none" stroke="#fff" stroke-width="2"/>
    <polygon points="210,24 396,210 210,396 24,210" fill="url(#g2)"/>
  </svg>
</section>

<section class="contact">
  <h2 class="section-title">Contact Form</h2>
  <div class="rule"></div>
  <div class="field" style="left:196px;top:162px;width:398px">Your Name*</div>
  <div class="field" style="left:606px;top:162px;width:398px">Last Name*</div>
  <div class="field" style="left:196px;top:218px;width:398px">Email address*</div>
  <div class="field" style="left:606px;top:218px;width:398px">Phone*</div>
  <div class="field" style="left:196px;top:274px;width:808px;height:112px">Message</div>
  <span class="btn-pill btn-send">Send</span>
</section>

<footer class="site-footer">
  <nav class="footer-nav"><span>HOME</span><span>SERVICES</span><span>ABOUT US</span><span>CONTACT</span></nav>
  <div class="legal">© 2021 Brindle Cove Homes &nbsp;|&nbsp; Legal &nbsp;|&nbsp; Terms of Use</div>
  <div class="social"><span></span><span></span><span></span></div>
</footer>

</body>
</html>
```